Professional Modern Website Design

We are a premium IT services provider to the financial industry based in London. Our company is called Veltra our current holding page is www.veltra-example.co.uk. We require a new website to match our new corporate identity. This project is for the design phase only. Development will be handled in-house. I have attached examples of wire frames we have developed (although open to suggestions for improvement) Our brand document that should demonstrate current brand, inc how we communicate to potential clients and finally mostly completed web-content.
We are looking for designers that can create something that sets us apart from our competitors.
Target Market(s)
IT Decision makers in Finance companies such as; hedge funds, private investment banks etc
Industry/Entity Type
Financial
Number of Pages Required
5+ page
Requirements
Must have
- hexagon elements in the design, unique design.
Nice to have
- Blog and social media feeds
Should not have
- Should not resemble a downloaded template

```html
<!DOCTYPE html>
<html lang="en">
<head>
<meta charset="utf-8">
<title>Veltra – IT Services for Finance</title>
<link rel="stylesheet" href="https://fonts.googleapis.com/css2?family=Open+Sans:wght@300;400;600;700&display=swap">
<style>
:root{
  --orange:#f37021;
  --orange-dark:#e0601a;
  --ink:#333;
  --grey:#777;
  --light:#f4f4f4;
  --dark:#1d1d1d;
  --white:#fff;
}
*{box-sizing:border-box;margin:0;padding:0}
html,body{width:1200px;height:2169px;overflow:hidden}
body{font-family:"Open Sans",Arial,sans-serif;color:var(--ink);background:var(--white);position:relative}
/* header */
.site-header{position:absolute;top:0;left:0;width:1200px;height:58px;background:var(--white);border-bottom:1px solid #eee}
.brand{position:absolute;left:241px;top:10px;display:flex;align-items:center;gap:10px}
.brand-mark{width:34px;height:34px;background:var(--orange)}
.brand-name{font-size:20px;font-weight:400;letter-spacing:5px;color:var(--grey)}
.main-nav{position:absolute;right:285px;top:21px;display:flex;gap:20px;font-size:10px;font-weight:600;color:#444}
.main-nav .active{color:var(--orange);border-bottom:2px solid var(--orange);padding-bottom:4px}
/* hero */
.hero{position:absolute;top:58px;left:0;width:1200px;height:417px;background:linear-gradient(180deg,#2a2a2a 0%,#474747 55%,#2e2e2e 100%)}
.hero-logo{position:absolute;left:0;width:1200px;top:40px;text-align:center}
.hero-logo .brand-mark{width:76px;height:76px;margin:0 auto 22px;display:block}
.hero-logo .brand-name{color:var(--white);font-size:20px;letter-spacing:8px}
.hero h1{position:absolute;top:188px;left:0;width:1200px;text-align:center;font-size:27px;font-weight:600;color:var(--white)}
.hero h1 em{font-style:normal;color:var(--orange)}
.hero-intro{position:absolute;top:246px;left:378px;width:444px;text-align:center;font-size:12px;line-height:19px;color:#eee}
.btn{display:inline-block;background:var(--orange);color:var(--white);font-size:13px;font-weight:600;padding:7px 26px}
.hero-cta{position:absolute;left:560px;top:326px}
.slider-dots{position:absolute;top:380px;left:832px;display:flex;gap:10px}
.slider-dots span{width:17px;height:17px;border-radius:50%;background:var(--white)}
.slider-dots span:first-child{background:var(--orange)}
/* decor */
.hex-field{position:absolute;background:radial-gradient(closest-side,#ececec,rgba(255,255,255,0))}
/* section headings */
.section-icon{position:absolute;left:580px;width:40px;height:40px;border-radius:50%;background:var(--white);border:3px solid var(--dark);display:flex;align-items:center;justify-content:center}
.section-title{position:absolute;left:0;width:1200px;text-align:center;font-size:26px;font-weight:600;color:var(--orange)}
.section-title span{color:var(--orange);font-weight:400}
.lead{position:absolute;top:565px;left:320px;width:560px;text-align:center;font-size:13px;line-height:21px;color:var(--grey)}
/* audience */
.audience{position:absolute;top:645px;left:282px;width:640px;display:flex;justify-content:space-between}
.persona{width:130px}
.persona svg{display:block;margin:0 auto 18px 8px}
.persona h3{font-size:13px;font-weight:700;color:#222;line-height:17px;margin-bottom:10px;min-height:17px}
.persona p{font-size:7px;line-height:11px;color:var(--grey)}
/* blog */
.blog-band{position:absolute;top:1046px;left:0;width:1200px;height:296px}
.blog-band svg{position:absolute;top:0;left:0}
.blog-post{position:absolute;top:1090px;left:287px;width:625px;color:var(--white)}
.blog-post h4{font-size:11px;font-weight:700;padding-bottom:10px;border-bottom:1px solid rgba(255,255,255,.5);margin-bottom:14px}
.blog-post p{font-size:10px;line-height:15px}
.btn-dark{position:absolute;top:1230px;left:287px;background:var(--dark);color:var(--white);font-size:10px;padding:6px 12px}
/* tweets */
.tweets{position:absolute;top:1468px;left:374px;width:520px}
.tweet{display:flex;gap:14px;height:51px}
.tweet-avatar{width:28px;height:28px;background:var(--orange);flex:none;margin-top:6px}
.tweet-handle{font-size:10px;color:var(--grey);margin-bottom:6px}
.tweet-text{font-size:11px;font-weight:600;color:#222}
.tweet-text span{font-weight:400}
/* offices */
.offices{position:absolute;top:1725px;left:0;width:1200px;height:280px;background:linear-gradient(180deg,#262626,#141414)}
.office{position:absolute;top:38px;color:var(--white)}
.office h5{font-size:22px;font-weight:400;margin-bottom:12px}
.office .addr{font-size:10px;line-height:15px;color:var(--orange);margin-bottom:8px}
.office .line{font-size:14px;font-weight:600;margin-bottom:6px}
.office .line b{font-size:10px;color:var(--orange);font-weight:400}
.map{position:absolute;left:773px;top:39px;width:143px;height:140px;background:linear-gradient(135deg,#d9d9d9,#bdbdbd);border:2px solid #fff}
.hotline{position:absolute;right:284px;text-align:right;color:var(--white);font-size:14px;font-weight:700}
.hotline b{color:var(--orange);font-weight:600}
/* footer */
.site-footer{position:absolute;top:2005px;left:0;width:1200px;height:164px;background:var(--light);text-align:center}
.site-footer .brand-mark{width:30px;height:30px;margin:28px auto 6px}
.site-footer .brand-name{font-size:11px;letter-spacing:4px}
.legal{font-size:9px;color:#999;margin-top:16px}
.socials{display:flex;justify-content:center;gap:5px;margin-top:10px}
.socials span{width:13px;height:13px;background:#999}
</style>
</head>
<body>

<header class="site-header">
  <div class="brand"><div class="brand-mark"></div><div class="brand-name">VELTRA</div></div>
  <nav class="main-nav"><span class="active">HOME</span><span>ABOUT US</span><span>SERVICES</span><span>PARTNERS</span><span>CLIENTS</span><span>CONTACT</span></nav>
</header>

<section class="hero" role="img" aria-label="Dark night skyline of city office towers">
  <div class="hero-logo"><div class="brand-mark"></div><div class="brand-name">VELTRA</div></div>
  <h1>You need <em>integration.</em> We're always there <em>with you.</em></h1>
  <p class="hero-intro">Veltra is one of the leading systems integrators to the world's finance sector. We are an extension of your business and our services portfolio has been built so you always have access to a complete partner.</p>
  <a class="btn hero-cta">About Us</a>
  <div class="slider-dots"><span></span><span></span><span></span><span></span></div>
</section>

<div class="hex-field" role="img" aria-label="Faint hexagon outline pattern" style="left:0;top:475px;width:160px;height:200px"></div>
<div class="hex-field" role="img" aria-label="Faint hexagon outline pattern" style="left:1040px;top:800px;width:160px;height:200px"></div>
<div class="hex-field" role="img" aria-label="Faint hexagon outline pattern" style="left:1030px;top:1310px;width:170px;height:200px"></div>

<div class="section-icon" style="top:478px">
  <svg width="20" height="16" viewBox="0 0 20 16"><circle cx="10" cy="5" r="3.2" fill="#1d1d1d"/><path d="M4 15c0-4 3-6 6-6s6 2 6 6z" fill="#1d1d1d"/><circle cx="3.5" cy="7" r="2" fill="#1d1d1d"/><circle cx="16.5" cy="7" r="2" fill="#1d1d1d"/></svg>
</div>
<h2 class="section-title" style="top:518px">Who <span>Are You?</span></h2>
<p class="lead">If you're part of a financial organisation, we have the power to help everyone work more efficiently, productively and profitably.</p>

<div class="audience">
  <article class="persona">
    <svg width="114" height="128" viewBox="0 0 114 128" role="img" aria-label="Photo of a hedge fund executive"><defs><linearGradient id="g1" x1="0" y1="0" x2="0" y2="1"><stop offset="0" stop-color="#8aa4c8"/><stop offset="1" stop-color="#3a3d58"/></linearGradient></defs><polygon points="57,0 114,32 114,96 57,128 0,96 0,32" fill="url(#g1)"/></svg>
    <h3>Senior Hedge Fund Manager/CEO</h3>
    <p>You need to demonstrate resilient, compliant systems to your investors while keeping costs in check. We design infrastructure that scales with your fund, protects your data and frees your team to focus on performance and returns.</p>
  </article>
  <article class="persona">
    <svg width="114" height="128" viewBox="0 0 114 128" role="img" aria-label="Photo of a finance director at work"><defs><linearGradient id="g2" x1="0" y1="0" x2="0" y2="1"><stop offset="0" stop-color="#e9e6e2"/><stop offset="1" stop-color="#7a6a63"/></linearGradient></defs><polygon points="57,0 114,32 114,96 57,128 0,96 0,32" fill="url(#g2)"/></svg>
    <h3>CFO</h3>
    <p>Technology spend should be predictable and measurable. Our managed services turn complex IT costs into clear monthly figures, with reporting that shows exactly where value is delivered across the business.</p>
  </article>
  <article class="persona">
    <svg width="114" height="128" viewBox="0 0 114 128" role="img" aria-label="Photo of an IT manager with hardware"><defs><linearGradient id="g3" x1="0" y1="0" x2="0" y2="1"><stop offset="0" stop-color="#c9b8a6"/><stop offset="1" stop-color="#5e5750"/></linearGradient></defs><polygon points="57,0 114,32 114,96 57,128 0,96 0,32" fill="url(#g3)"/></svg>
    <h3>IT Manager/CTO</h3>
    <p>Integration with existing platforms and data is central to every project. We work alongside your team to plan, build and support secure systems, giving you a single trusted partner for the whole lifecycle.</p>
  </article>
  <article class="persona">
    <svg width="114" height="128" viewBox="0 0 114 128" role="img" aria-label="Photo of office employees meeting"><defs><linearGradient id="g4" x1="0" y1="0" x2="0" y2="1"><stop offset="0" stop-color="#b9c0d2"/><stop offset="1" stop-color="#4a4f6a"/></linearGradient></defs><polygon points="57,0 114,32 114,96 57,128 0,96 0,32" fill="url(#g4)"/></svg>
    <h3>Employees</h3>
    <p>People do their best work with tools that simply work. We provide fast support, reliable devices and secure remote access, so staff can stay productive wherever the markets take them.</p>
  </article>
</div>

<h2 class="section-title" style="top:982px">Our <span>BLOG</span></h2>
<div class="blog-band">
  <svg width="1200" height="296" viewBox="0 0 1200 296"><polygon points="0,0 1200,0 1200,268 625,268 600,296 575,268 0,268" fill="#f37021"/></svg>
</div>
<div class="section-icon" style="top:1026px">
  <svg width="18" height="18" viewBox="0 0 18 18"><rect x="2" y="2" width="14" height="14" rx="3" fill="none" stroke="#1d1d1d" stroke-width="2"/><rect x="5" y="6" width="8" height="2" fill="#1d1d1d"/><rect x="5" y="10" width="6" height="2" fill="#1d1d1d"/></svg>
</div>
<article class="blog-post">
  <h4>CLOUD GROWTH IN THE FINANCIAL SECTOR</h4>
  <p>Cloud is slowly gaining popularity within the financial sector, but many companies have been slow to adopt it and put in place a proper strategy for cloud. Unsurprisingly, the main concerns are over the security of cloud systems. A survey recently conducted by the Cloud Trust Forum revealed that 61 per cent of respondents had a cloud strategy in the formative stages in their company. 47 per cent of those said they had plans to use a combination of in-house IT, public and private cloud. 18 per cent planned to use private clouds. None of those surveyed had plans to primarily use public cloud.</p>
</article>
<a class="btn-dark">Read More</a>

<div class="section-icon" style="top:1358px">
  <svg width="16" height="16" viewBox="0 0 16 16"><circle cx="3" cy="13" r="2" fill="#1d1d1d"/><path d="M1 7a8 8 0 0 1 8 8M1 2a13 13 0 0 1 13 13" fill="none" stroke="#1d1d1d" stroke-width="2"/></svg>
</div>
<h2 class="section-title" style="top:1398px">FOLLOW <span>Us</span></h2>

<div class="tweets">
  <div class="tweet"><div class="tweet-avatar"></div><div><div class="tweet-handle">@Veltra_</div><div class="tweet-text">Tom Crane spills the beans on Orbipay rollout <span>http://sh.ex/jGeXL</span></div></div></div>
  <div class="tweet"><div class="tweet-avatar"></div><div><div class="tweet-handle">@Veltra_</div><div class="tweet-text">How the Lumen Pictures attack changed the rules of cybersecurity <span>http://sh.ex/jGeMj</span></div></div></div>
  <div class="tweet"><div class="tweet-avatar"></div><div><div class="tweet-handle">@Veltra_</div><div class="tweet-text">Trust in the digital world: Is it at an all time low? <span>http://sh.ex/jGesQ</span></div></div></div>
  <div class="tweet"><div class="tweet-avatar"></div><div><div class="tweet-handle">@Veltra_</div><div class="tweet-text">Building an emergency internet in the white spaces <span>http://sh.ex/jGdwH</span></div></div></div>
</div>

<section class="offices" role="img" aria-label="Dark city skyline backdrop behind office details">
  <div class="office" style="left:284px">
    <h5>LONDON OFFICE</h5>
    <div class="addr">48 ASHCOMBE STREET, MARYLEBONE<br><br>LONDON W1X 9QA</div>
    <div class="line">TEL: <b>+44 20 7946 0321</b></div>
    <div class="line">E-MAIL: <b>INFO@VELTRA-EXAMPLE.CO.UK</b></div>
  </div>
  <div class="office" style="left:530px">
    <h5>ESSEX OFFICE</h5>
    <div class="addr">7 HARROW WORKS, HARROW AVENUE<br><br>LEIGH, ESSEX SS9 4ZZ</div>
    <div class="line">TEL: <b>+44 20 7946 0321</b></div>
    <div class="line">E-MAIL: <b>INFO@VELTRA-EXAMPLE.CO.UK</b></div>
  </div>
  <div class="map" role="img" aria-label="Street map showing office location"></div>
  <div class="hotline" style="top:210px">SUPPORT: <b>+44 20 7946 0321</b></div>
  <div class="hotline" style="top:240px">SALES: <b>+44 20 7946 0322</b></div>
</section>

<footer class="site-footer">
  <div class="brand-mark"></div>
  <div class="brand-name">VELTRA</div>
  <div class="legal">© Veltra Limited - Company Registration No. 0918273 Incorporated in England and Wales</div>
  <div class="socials"><span></span><span></span><span></span><span></span><span></span><span></span></div>
</footer>

</body>
</html>
```